Vela Stewardship Business Card design

We need a creative business card design for our hospitality management company
We need the following information:
Our business Logo: Vela Stewardship
Name: Mara Dobrinsky
Phone number: 0458 317 642
Email: mara@velastewardship.com.au
Address: 214/53 Penrose Street, South Melbourne 3206
Web: www.velastewardship.com.au
I need the design to be a working file so that I can insert the names and numbers of the other staff members of our business.
The cards need to be 90 x 40mm
Thanks
Industry/Entity Type
Hospitality
Look and feel

```html
<!DOCTYPE html>
<html lang="en">
<head>
<meta charset="utf-8">
<title>Vela Stewardship – Business Card</title>
<link rel="stylesheet" href="https://fonts.googleapis.com/css2?family=Arimo:wght@400;700&display=swap">
<style>
  :root {
    --stage: #e9e6e1;
    --card-dark: #141414;
    --card-mid: #2c2c2c;
    --gold: #f2b21b;
    --gold-deep: #e6a00f;
    --ink: #1a1a1a;
    --text-light: #f2f2f2;
    --icon-gold: #f0a81c;
  }
  * { box-sizing: border-box; margin: 0; padding: 0; }
  html, body {
    width: 1200px;
    height: 800px;
    overflow: hidden;
    background: var(--stage);
  }
  .stage {
    width: 1200px;
    height: 800px;
    display: flex;
    align-items: center;
    justify-content: center;
  }
  .card {
    position: relative;
    width: 1000px;
    height: 444px;
    border-radius: 6px;
    overflow: hidden;
    background: radial-gradient(ellipse 60% 70% at 58% 38%, var(--card-mid) 0%, var(--card-dark) 75%);
    box-shadow: 0 18px 40px rgba(0,0,0,0.25);
    font-family: "Arimo", Arial, sans-serif;
  }
  .brand {
    position: absolute;
    top: 60px;
    left: 560px;
    display: flex;
    flex-direction: column;
    align-items: center;
    gap: 22px;
  }
  .brand-square {
    width: 88px;
    height: 88px;
    background: var(--gold);
    border-radius: 4px;
  }
  .brand-name {
    font-weight: 700;
    font-size: 38px;
    letter-spacing: 0.5px;
    color: var(--gold);
    text-transform: uppercase;
    white-space: nowrap;
  }
  .name-band {
    position: absolute;
    left: 0;
    right: 0;
    top: 256px;
    height: 40px;
    background: linear-gradient(90deg, var(--gold) 0%, var(--gold-deep) 60%, rgba(230,160,15,0.35) 88%, rgba(230,160,15,0) 100%);
  }
  .person-name {
    position: absolute;
    left: 56px;
    top: 258px;
    font-weight: 700;
    font-size: 30px;
    color: var(--ink);
    line-height: 36px;
  }
  .contact {
    position: absolute;
    display: flex;
    flex-direction: column;
    gap: 12px;
    color: var(--text-light);
    font-size: 22px;
  }
  .contact-left { left: 56px; top: 322px; }
  .contact-right { left: 630px; top: 316px; }
  .contact-row {
    display: flex;
    align-items: flex-start;
    gap: 12px;
    line-height: 28px;
  }
  .contact-row svg { flex: none; margin-top: 5px; }
</style>
</head>
<body>
<main class="stage">
  <section class="card" aria-label="Vela Stewardship business card">
    <div class="brand">
      <div class="brand-square" aria-hidden="true"></div>
      <div class="brand-name">Vela Stewardship</div>
    </div>

    <div class="name-band" aria-hidden="true"></div>
    <h1 class="person-name">Mara Dobrinsky</h1>

    <div class="contact contact-left">
      <div class="contact-row">
        <svg width="16" height="20" viewBox="0 0 16 20" aria-hidden="true">
          <rect x="2" y="1" width="12" height="18" rx="2" fill="var(--icon-gold)"/>
          <rect x="4" y="3.5" width="8" height="6" fill="var(--card-dark)"/>
          <rect x="4" y="12" width="2" height="1.6" fill="var(--card-dark)"/>
          <rect x="7" y="12" width="2" height="1.6" fill="var(--card-dark)"/>
          <rect x="10" y="12" width="2" height="1.6" fill="var(--card-dark)"/>
          <rect x="4" y="15" width="2" height="1.6" fill="var(--card-dark)"/>
          <rect x="7" y="15" width="2" height="1.6" fill="var(--card-dark)"/>
          <rect x="10" y="15" width="2" height="1.6" fill="var(--card-dark)"/>
        </svg>
        <span>0458 317 642</span>
      </div>
      <div class="contact-row">
        <svg width="20" height="16" viewBox="0 0 20 16" aria-hidden="true">
          <rect x="1" y="2" width="18" height="12" rx="1.5" fill="var(--icon-gold)"/>
          <path d="M1.5 3 L10 9.5 L18.5 3" fill="none" stroke="var(--card-dark)" stroke-width="1.6"/>
        </svg>
        <span>mara@velastewardship.com.au</span>
      </div>
    </div>

    <div class="contact contact-right">
      <div class="contact-row">
        <svg width="22" height="20" viewBox="0 0 22 20" aria-hidden="true">
          <path d="M11 1 L21 10 H18 V19 H13 V13 H9 V19 H4 V10 H1 Z" fill="var(--icon-gold)"/>
        </svg>
        <span>214/53 Penrose Street,<br>South Melbourne 3206</span>
      </div>
    </div>
  </section>
</main>
</body>
</html>
```